Best Seller Book Cover ...

Book Title: Stop Chasing Meaning: Pick a Trail, Keep to That Trail, Mind the Geese

Edgy, Minimalist, Compelling, Attractive, Classy design.

Very clean. See examples.,

Target Market(s)

Mid Life People ages 38-55 Male and Female equally

Requirements

Nice to have
• Nice to Have:

Minimalist and eye catching ( i have loaded a few examples of what this means)
Should not have
• Clip Art
Clutter

```html
<!DOCTYPE html>
<html lang="en">
<head>
<meta charset="utf-8">
<title>Stop Chasing Meaning — Book Cover</title>
<link rel="stylesheet" href="https://fonts.googleapis.com/css2?family=Bebas+Neue&family=Quicksand:wght@600;700&display=swap">
<style>
  :root {
    --backdrop: #4a4a4a;
    --paper: #f0f0ee;
    --paper-shade: #e4e4e2;
    --ink: #1c1c1c;
    --ink-soft: #555555;
    --accent: #f5a033;
    --ghost: #c4c4c4;
    --art-dark: #151515;
    --art-mid: #3a3a3a;
  }
  * { box-sizing: border-box; margin: 0; padding: 0; }
  html, body {
    width: 1200px;
    height: 720px;
    overflow: hidden;
    background: var(--backdrop);
  }
  .canvas {
    position: relative;
    width: 1200px;
    height: 720px;
  }
  .cover {
    position: absolute;
    left: 390px;
    top: 40px;
    width: 420px;
    height: 640px;
    overflow: hidden;
    background: radial-gradient(ellipse at 40% 30%, var(--paper) 0%, var(--paper) 55%, var(--paper-shade) 100%);
    text-align: center;
  }
  .cover > * {
    position: absolute;
    left: 0;
    right: 0;
  }
  .cover-title {
    top: 56px;
    font-family: "Bebas Neue", sans-serif;
    font-weight: 400;
    font-size: 46px;
    line-height: 1.05;
    letter-spacing: 0.16em;
    color: var(--ink);
  }
  .cover-subtitle {
    top: 176px;
    font-family: "Quicksand", sans-serif;
    font-weight: 700;
    font-size: 11.5px;
    line-height: 1.9;
    letter-spacing: 0.05em;
    color: var(--ink-soft);
  }
  .cover-subtitle .ghost { color: var(--ghost); }
  .cover-subtitle .accent { color: var(--accent); }
  .cover-art {
    top: 246px;
    left: 115px;
    width: 190px;
    height: 280px;
  }
  .cover-author {
    top: 560px;
    font-family: "Quicksand", sans-serif;
    font-weight: 700;
    font-size: 12px;
    letter-spacing: 0.14em;
    color: var(--ink);
  }
  .cover-publisher {
    top: 598px;
    font-family: "Quicksand", sans-serif;
    font-weight: 600;
    font-size: 11px;
    letter-spacing: 0.1em;
    color: var(--ink-soft);
  }
</style>
</head>
<body>
  <main class="canvas">
    <article class="cover">
      <h1 class="cover-title">Stop Chasing<br>Meaning</h1>
      <p class="cover-subtitle">
        Pick a <span class="accent">Trail</span>, Keep to <span class="ghost">That</span> Trail,<br>
        <span class="accent">Mind</span> the <span class="accent">Geese</span>.
      </p>
      <svg class="cover-art" viewBox="0 0 190 280" role="img" aria-label="Abstract cut-out illustration: a dark irregular opening filled with white organic shapes">
        <defs>
          <linearGradient id="art-tone" x1="0" y1="0" x2="0" y2="1">
            <stop offset="0" stop-color="#151515"/>
            <stop offset="1" stop-color="#3a3a3a"/>
          </linearGradient>
        </defs>
        <path fill="url(#art-tone)" d="M14 18 C30 4 58 10 80 6 C104 2 128 12 150 6 C170 2 184 20 182 44 C180 90 188 140 184 190 C182 226 186 254 170 270 C140 280 110 272 80 278 C52 282 28 276 12 262 C4 232 10 196 6 158 C2 110 8 60 14 18 Z"/>
      </svg>
      <p class="cover-author">AUTHOR'S NAME</p>
      <p class="cover-publisher">Publisher</p>
    </article>
  </main>
</body>
</html>
```